Business Card Design for Fashion Tech Startup

Dear designers, we need a business card for Asia's premier fashion tech startup.!

PebbleHop is discovery e-commerce destination for busy, discerning parents in Asia featuring leading independent designers of baby, kids fashion apparel and sustainable brands from around the world.

PebbleHop is a modern, contemporary fashion tech startup targeting well-educated, well travelled and affluent parents. We're NOT your typical kiddy store!! Our design philosophy & e-commerce site is more like Vask.com, Orimesa.com, Pondwick.com, Farthollow.com.
Updates

Hi, size of the business card should be 84mm X 55mm. Would appreciate some business card layouts in Portrait as added consideration, i fancy the idea of a Portrait business card. What's important is that the business card should pique the receiver's interest to log onto the website to learn more. Many thanks and love forward to the designs!

Target Market(s)

Though modern, classy in look, feel & positioning, PebbleHop does possess a cheeky, fun-loving personality as depicted by its logo and the segment it targets (baby, kids) though the key decision makers i.e primarily mums between 25-40 who are well educated/travelled, local & expatriates, internet/digitally savvy, mid-high income working mums.

Industry/Entity Type

E-Commerce

Requirements
Must have
• Name, designation, email, phone & mobile number.
Company url : www.pebblehop.sg
Slogan : Discovery e-commerce destination for discerning, busy parents
Nice to have
• Call to Action such as a Discount code offering 10% discount
or asking people to "Like" us on our Chatterly page/Chatterly URL

```html
<!DOCTYPE html>
<html lang="en">
<head>
<meta charset="utf-8">
<title>PebbleHop Business Card</title>
<link rel="stylesheet" href="https://fonts.googleapis.com/css2?family=Exo+2:wght@500&family=Open+Sans:wght@400;600&family=Ubuntu:wght@500;700&display=swap">
<style>
  :root {
    --stage: #a9a9a9;
    --navy: #2f5a74;
    --coral: #f2866a;
    --link-blue: #2a4fa3;
    --paper: #ffffff;
    --ink-light: #f4f7f9;
  }
  html, body {
    margin: 0;
    padding: 0;
    width: 1200px;
    height: 1000px;
    overflow: hidden;
    background: var(--stage);
  }
  .canvas {
    position: relative;
    width: 1200px;
    height: 1000px;
  }
  .card {
    position: absolute;
    left: 75px;
    width: 297px;
    height: 454px;
    background: var(--paper);
    box-shadow: 4px 5px 6px rgba(0,0,0,0.45);
    overflow: hidden;
    font-family: "Open Sans", sans-serif;
  }
  .card--front { top: 27px; }
  .card--back { top: 503px; }

  /* Front */
  .front-band {
    position: absolute;
    left: 0; top: 0;
    width: 100%;
    height: 296px;
    background: var(--navy);
  }
  .holder-name {
    position: absolute;
    top: 52px;
    width: 100%;
    text-align: center;
    font-family: "Exo 2", sans-serif;
    font-weight: 500;
    font-size: 24px;
    letter-spacing: 0.5px;
    color: var(--coral);
    margin: 0;
  }
  .holder-title {
    position: absolute;
    top: 84px;
    width: 100%;
    text-align: center;
    font-size: 11px;
    color: var(--ink-light);
    margin: 0;
  }
  .contact-list {
    position: absolute;
    left: 74px;
    top: 198px;
    margin: 0;
    padding: 0;
    list-style: none;
  }
  .contact-list li {
    display: flex;
    align-items: center;
    height: 19.5px;
    font-size: 12px;
    color: var(--ink-light);
  }
  .contact-icon {
    width: 12px;
    height: 12px;
    margin-right: 10px;
    flex: none;
  }
  .brand-lockup {
    position: absolute;
    top: 318px;
    left: 0;
    width: 100%;
    display: flex;
    justify-content: center;
    align-items: center;
    gap: 10px;
  }
  .brand-dot {
    width: 36px;
    height: 36px;
    border-radius: 50%;
    background: var(--coral);
  }
  .brand-name {
    font-family: "Ubuntu", sans-serif;
    font-weight: 700;
    font-size: 22px;
    color: var(--coral);
  }
  .social-cta {
    position: absolute;
    top: 380px;
    width: 100%;
    text-align: center;
    font-family: "Ubuntu", sans-serif;
    font-weight: 500;
    color: var(--link-blue);
  }
  .social-cta__lead { font-size: 14px; margin: 0; }
  .social-cta__url {
    display: flex;
    justify-content: center;
    align-items: center;
    gap: 8px;
    font-size: 14px;
    margin: 2px 0 0;
  }
  .social-square {
    width: 20px;
    height: 20px;
    background: var(--link-blue);
    border-radius: 3px;
  }

  /* Back */
  .back-shape {
    position: absolute;
    left: 0; top: 0;
    width: 297px;
    height: 454px;
  }
  .illustration-area {
    position: absolute;
    left: 33px;
    top: 40px;
    width: 230px;
    height: 200px;
    border-radius: 50%;
    background: radial-gradient(circle at 50% 45%, #fbd5c8 0%, #f5a892 55%, #e9b0a2 75%, #c9d5de 100%);
  }
  .back-brand {
    position: absolute;
    top: 208px;
    width: 100%;
    text-align: center;
    font-family: "Ubuntu", sans-serif;
    font-weight: 700;
    font-size: 21px;
    color: var(--coral);
    margin: 0;
  }
  .slogan {
    position: absolute;
    top: 378px;
    left: 15px;
    right: 15px;
    text-align: center;
    font-weight: 600;
    font-size: 13px;
    line-height: 18px;
    color: var(--coral);
    margin: 0;
  }
</style>
</head>
<body>
<main class="canvas">

  <section class="card card--front" aria-label="Business card front">
    <div class="front-band"></div>
    <h1 class="holder-name">Marla Quint</h1>
    <p class="holder-title">Designation</p>
    <ul class="contact-list">
      <li>
        <svg class="contact-icon" viewBox="0 0 12 12" aria-hidden="true"><rect x="0" y="0" width="12" height="12" rx="2" fill="#f4f7f9"/><rect x="3.5" y="2" width="5" height="8" rx="1" fill="#2f5a74"/></svg>
        08 5550 3917
      </li>
      <li>
        <svg class="contact-icon" viewBox="0 0 12 12" aria-hidden="true"><rect x="0" y="0" width="12" height="12" rx="2" fill="#f4f7f9"/><path d="M3 2.5 L5 2.5 L5.5 4.5 L4.5 5.2 Q5.5 7 7 7.6 L7.7 6.6 L9.5 7.2 L9.5 9.2 Q5 9.5 3 4.5 Z" fill="#2f5a74"/></svg>
        08 5550 3917
      </li>
      <li>
        <svg class="contact-icon" viewBox="0 0 12 12" aria-hidden="true"><rect x="0" y="0" width="12" height="12" rx="2" fill="#f4f7f9"/><rect x="2" y="3.5" width="8" height="5.5" fill="none" stroke="#2f5a74" stroke-width="1"/><path d="M2 3.5 L6 6.5 L10 3.5" fill="none" stroke="#2f5a74" stroke-width="1"/></svg>
        marla@pebblehop.sg
      </li>
      <li>
        <svg class="contact-icon" viewBox="0 0 12 12" aria-hidden="true"><rect x="0" y="0" width="12" height="12" rx="2" fill="#f4f7f9"/><circle cx="6" cy="6" r="3.6" fill="none" stroke="#2f5a74" stroke-width="1"/><path d="M2.4 6 H9.6 M6 2.4 Q4 6 6 9.6 M6 2.4 Q8 6 6 9.6" fill="none" stroke="#2f5a74" stroke-width="0.8"/></svg>
        www.pebblehop.sg
      </li>
    </ul>
    <div class="brand-lockup">
      <span class="brand-dot" aria-hidden="true"></span>
      <span class="brand-name">PebbleHop</span>
    </div>
    <div class="social-cta">
      <p class="social-cta__lead">Like us on</p>
      <p class="social-cta__url"><span class="social-square" aria-hidden="true"></span>www.chatterly.com/pebblehop</p>
    </div>
  </section>

  <section class="card card--back" aria-label="Business card back">
    <svg class="back-shape" viewBox="0 0 297 454" aria-hidden="true">
      <path d="M0 175 C25 300 170 345 297 318 L297 454 L0 454 Z" fill="#2f5a74"/>
      <path d="M0 175 C25 300 170 345 297 318" fill="none" stroke="#f2866a" stroke-width="4"/>
    </svg>
    <div class="illustration-area" role="img" aria-label="Round cluster of small coral and navy baby and kids item illustrations around the brand emblem"></div>
    <p class="back-brand">PebbleHop.sg</p>
    <p class="slogan">Discovery e-commerce destination for discerning, busy parents</p>
  </section>

</main>
</body>
</html>
```